Product sheet for managing talented people!

We need a new product sheet to describe our method of helping organisations to manage their talented people! We have selected a rowing team as the graphical theme (sample attached - please select or suggest a new picture if you want). We have also attached a powerpoint slide with our model (this is the service we offer).

FRONT PAGE

We are looking for an eye-catching front page that uses our 1. "Kestrel Skills Model"; 2. a picture of a rowing team of 8, and 3. our logo and 1800 KESTRL phone number (1800 537 875).

Step 1 - Assess key positions to determine your Talent Management Priorities.

Step 2 - Organisational psychology support helps individuals self-evaluate (see page 2 for details).

Step 3 - Facilitate agreement with manager and embed best-practice in organisational fairness.

Step 4 - Tailor career development and redeployment options based on shared understanding.

Step 5 - Evaluate ROI for individual performance and engagement.

BACK PAGE

The second page will have more detail of each of the talent categories also included in the powerpoint slide. Logo attached also. Please also view our website as the graphics should give you a sense of the look and feel of our brand - www.kestrelsm.com.au We have also added another flyer that we still use - please do not reverse the logo on this project - use in current form. CORPORATE LOGO / COLOUR GUIDE
C100 M50 Y0 K0
C100 M50 Y0 K0
C100 M50 Y0 K0
Gradient
C100 M60 Y0 K40
C100 M45 Y0 K0
C100 M20 Y0 K0
C70 M0 Y0 K0
PMS 2935 C
PMS 2935 C 75% Tint
PMS 2935 C
PMS Process Cyan C

The successful flyer will need to be print ready (as per attached example) and in pdf form so that we can print and/or send as a PDF.

Thanks.

Target Market(s)

Human Resource Managers in business and government.

Industry/Entity Type

Product

Requirements
Must have
• Eye-catching graphics with a rowing team theme. Colours consistent with our corporate colour codes.
Nice to have
• Please add small "trademark" symbol to the logo. This is small TM in a circle and usually placed at top right hand of logo. PLease add our website address www.kestrelsm.com
Should not have
• Please do not "reverse" the logo - use as is.

```html
<!DOCTYPE html>
<html lang="en">
<head>
<meta charset="utf-8">
<title>Kestrel Skills Management – Product Sheet</title>
<link rel="stylesheet" href="https://fonts.googleapis.com/css2?family=Titillium+Web:wght@400;600;700&family=Lato:ital@1&display=swap">
<style>
  :root {
    --brand-blue: #1b4a93;
    --brand-blue-deep: #133a7a;
    --brand-light: #8fb0ea;
    --ink-black: #1c1c1e;
    --paper: #ffffff;
    --canvas: #e6e6e6;
    --text-dark: #232323;
  }
  * { margin: 0; padding: 0; box-sizing: border-box; }
  html, body { width: 1200px; height: 1200px; overflow: hidden; background: var(--canvas); }
  body { font-family: "Titillium Web", sans-serif; }

  .sheet {
    position: absolute; left: 190px; top: 20px;
    width: 820px; height: 1160px;
    background: var(--paper);
    overflow: hidden;
    box-shadow: 0 6px 24px rgba(0,0,0,.18);
  }
  .sheet-shapes { position: absolute; inset: 0; }

  .brand { position: absolute; left: 40px; width: 380px; top: 150px; text-align: center; color: var(--brand-blue); font-weight: 600; }
  .brand-name { font-size: 70px; letter-spacing: 4px; line-height: 1; }
  .brand-sub { font-size: 15px; letter-spacing: 3px; margin-top: 6px; }

  .headline { position: absolute; left: 42px; top: 320px; color: var(--paper); font-weight: 600; font-size: 26px; line-height: 1.15; text-transform: uppercase; }

  .steps { position: absolute; left: 0; top: 418px; width: 430px; list-style: none; color: var(--paper); }
  .step { position: relative; padding-left: 53px; font-size: 17.5px; font-weight: 600; line-height: 1.3; }
  .step + .step { margin-top: 22px; }
  .step-num {
    position: absolute; left: 0; top: 2px; width: 42px; height: 30px;
    background: var(--paper); color: var(--brand-blue);
    clip-path: polygon(0 0, 100% 0, 82% 100%, 0 100%);
    font-weight: 700; font-size: 26px; line-height: 30px; text-align: center; padding-right: 6px;
  }
  .step-note { font-family: "Lato", sans-serif; font-style: italic; font-weight: 400; font-size: 11.5px; line-height: 1.4; margin-top: 14px; padding-right: 10px; }

  .contact {
    position: absolute; left: 44px; top: 862px; width: 408px; height: 188px;
    background: linear-gradient(180deg, #ffffff 0%, #e9e9e9 100%);
    border-radius: 10px 10px 0 0;
    padding: 24px 18px 0 18px;
  }
  .contact-text { color: var(--text-dark); font-size: 17px; font-weight: 600; line-height: 1.25; }
  .contact-call { color: var(--brand-blue); font-size: 21px; font-weight: 600; line-height: 1.2; margin-top: 22px; }

  .web { position: absolute; left: 46px; top: 1095px; color: var(--paper); font-size: 21px; font-weight: 600; letter-spacing: 3px; }

  .photo {
    position: absolute; border: 4px solid var(--paper); border-radius: 12px;
    box-shadow: 0 4px 10px rgba(0,0,0,.45);
  }
  .photo-crew-side { left: 430px; top: 45px; width: 338px; height: 168px; background: linear-gradient(180deg, #b74a4a 0%, #3558a8 45%, #d6d08a 80%, #8a8d6a 100%); }
  .photo-crew-top { left: 512px; top: 672px; width: 252px; height: 446px; background: linear-gradient(180deg, #4a6680 0%, #2f4a63 50%, #3b5870 100%); }

  .model-title {
    position: absolute; left: 470px; top: 240px; width: 298px; height: 42px;
    background: linear-gradient(180deg, #ffffff, #dcdcdc);
    border-radius: 12px; color: var(--brand-blue);
    font-size: 26px; font-weight: 600; line-height: 42px; text-align: center;
  }
  .model-list { position: absolute; left: 468px; top: 300px; width: 340px; list-style: none; color: var(--paper); font-size: 17px; line-height: 1.45; }
  .model-item { padding: 5px 0 6px; border-bottom: 1px solid rgba(255,255,255,.12); }
  .model-term { color: var(--brand-light); font-style: italic; font-weight: 600; }
</style>
</head>
<body>
<main class="sheet">
  <svg class="sheet-shapes" viewBox="0 0 820 1160" width="820" height="1160" aria-hidden="true">
    <path d="M0,295 C150,268 300,250 480,236 L820,236 V1060 H0 Z" fill="var(--brand-blue)"/>
    <path d="M508,0 C458,150 428,300 428,480 C428,700 488,900 548,1060" fill="none" stroke="var(--paper)" stroke-width="20"/>
    <path d="M528,0 H820 V1160 H0 V1060 H560 C500,900 440,700 440,480 C440,300 470,150 528,0 Z" fill="var(--ink-black)"/>
    <path d="M600,1010 C680,1050 750,1065 820,1070 V1108 C740,1105 660,1090 600,1060 Z" fill="var(--brand-blue)"/>
    <rect x="0" y="1056" width="820" height="4" fill="var(--paper)"/>
  </svg>

  <header class="brand">
    <div class="brand-name">KESTREL</div>
    <div class="brand-sub">SKILLS MANAGEMENT</div>
  </header>

  <h1 class="headline">Executive Coaching and<br>Career Development Experts</h1>

  <ol class="steps">
    <li class="step"><span class="step-num">1</span>Assess key positions to determine your Talent Management Priorities.
      <p class="step-note">Offers several levels of career transition support allowing you to select the program features that you believe are right for your departing employee. These program options are detailed below, and can be modified to suit your needs. All programs include reporting on client progress and outcomes.</p>
    </li>
    <li class="step"><span class="step-num">2</span>Organisational psychology support helps individuals self-evaluate</li>
    <li class="step"><span class="step-num">3</span>Facilitate agreement with manager an embed best-practice in organisational fairness.</li>
    <li class="step"><span class="step-num">4</span>Tailor career development and redeployment options based on shared understanding.</li>
    <li class="step"><span class="step-num">5</span>Evaluate ROI for individual performance and engagement.</li>
  </ol>

  <section class="contact">
    <p class="contact-text">Kestrel has first class offices in all capital cities and can provide on-site consultations with your key people by arrangement.</p>
    <p class="contact-call">For a confidential discussion or advice<br>1800 KESTRL (1800 537 875)</p>
  </section>

  <p class="web">www.kestrelsm.com.au</p>

  <div class="photo photo-crew-side" role="img" aria-label="Side view of a rowing crew in red and blue kit pulling oars"></div>

  <h2 class="model-title">Kestrel Skills Model</h2>
  <ul class="model-list">
    <li class="model-item"><span class="model-term">Exit</span> – planned or managed</li>
    <li class="model-item"><span class="model-term">Developing</span> - high risk/high reward</li>
    <li class="model-item"><span class="model-term">Contributing</span> - probable flight risk</li>
    <li class="model-item"><span class="model-term">Emerging</span> – manage career aspirations</li>
    <li class="model-item"><span class="model-term">Elite</span> – mission critical or<br>market-sensitive</li>
    <li class="model-item"><span class="model-term">Target</span> – strategic external hire<br>with market implications</li>
  </ul>

  <div class="photo photo-crew-top" role="img" aria-label="Overhead view of an eight-person rowing crew on the water"></div>
</main>
</body>
</html>
```